Quotation and Scripture Design

We are a marketing firm looking for a graphic designer who is gifted in the merging of typestyles, colors, and composition into images suitable for framing in the home or office. The design criteria is quite simple, (1) keep it fresh without looking dated or religious, and (2) push the envelope a little with good, solid graphic design. Phase one will involve building our inventory of original artwork to fifty or more pieces to be marketed online. For phase two in addition to a line of greeting cards, we will also offer art pieces reproduced by laser engravers, CNC routers, chemical etching, and digital printers. For this reason it is necessary that all art files be submitted in a vector format.

Target Market(s)

Professional women and men who appreciate and purchase gallery quality artwork.

Industry/Entity Type

Graphic Designer

Requirements
Must have
• Selection of the designer will be based on their graphic interruption of the following two quotations.
Quotation No. 1 - Romans 8:28
And we know that all things work together for good to those who love God, to those who are called according to His purpose.
Quotation No. 2 -Jeremiah 29:11
For I know the plans I have for you, declares the Lord. Plans to prosper you and not to harm you. Plans to give you hope and a future.
Design one of these two formats to fit a 8" x10" frame, and the other to fit a 12" x 12" frame.
Nice to have
• Rich colors, fresh typestyles . . . please no Times Roman. Bold, creative composition is what we are looking for.
Should not have
• Dated, religious artwork found in the local bible bookstore is a very good example of what we DO NOT want. If it is not something you would purchase for yourself or a friend, more than likely it won't meet our criteria.

```html
<!DOCTYPE html>
<html lang="en">
<head>
<meta charset="utf-8">
<title>Romans 8:28 — All Things Work Together for Good</title>
<link rel="stylesheet" href="https://fonts.googleapis.com/css2?family=Antonio:wght@100;200;300&display=swap">
<style>
  :root {
    --frame: #ecebef;
    --ink: #fbf8fb;
    --sky-top: #8c9796;
    --sky-mid: #b7bcae;
    --horizon: #ead9a6;
    --sea: #b0a6b4;
    --sea-low: #8e7f93;
    --shore: #5b4960;
    --shore-deep: #3f3044;
  }
  html, body {
    margin: 0;
    padding: 0;
    width: 958px;
    height: 1200px;
    overflow: hidden;
    background: var(--frame);
  }
  .poster {
    display: block;
    width: 958px;
    height: 1200px;
  }
  .verse {
    font-family: "Antonio", "Oswald", sans-serif;
    fill: var(--ink);
  }
  .verse-lead { font-weight: 200; font-size: 34px; }
  .verse-headline { font-weight: 100; font-size: 192px; }
  .verse-subhead { font-weight: 200; font-size: 74px; }
  .verse-tail { font-weight: 200; font-size: 33px; }
  .verse-reference { font-weight: 300; font-size: 42px; }
  .rule, .headline-box {
    stroke: var(--ink);
    fill: none;
  }
</style>
</head>
<body>
<svg class="poster" viewBox="0 0 958 1200" xmlns="http://www.w3.org/2000/svg">
  <defs>
    <linearGradient id="scene-tones" x1="0" y1="0" x2="0" y2="1">
      <stop offset="0" stop-color="var(--sky-top)"/>
      <stop offset="0.18" stop-color="var(--sky-mid)"/>
      <stop offset="0.27" stop-color="var(--horizon)"/>
      <stop offset="0.29" stop-color="var(--sea)"/>
      <stop offset="0.52" stop-color="var(--sea-low)"/>
      <stop offset="0.70" stop-color="var(--shore)"/>
      <stop offset="1" stop-color="var(--shore-deep)"/>
    </linearGradient>
  </defs>

  <rect class="frame" width="958" height="1200" fill="var(--frame)"/>
  <rect class="scene" x="25" y="25" width="910" height="1150" fill="url(#scene-tones)"
        role="img" aria-label="Calm sea at dusk with weathered wooden posts running out over a pebble beach"/>

  <text class="verse verse-lead" x="356" y="148" textLength="241" lengthAdjust="spacingAndGlyphs">AND WE KNOW THAT</text>

  <text class="verse verse-headline" x="123" y="544" textLength="705" lengthAdjust="spacingAndGlyphs">ALL THINGS</text>

  <rect class="headline-box" x="114" y="559" width="728" height="91" stroke-width="1.2"/>
  <text class="verse verse-subhead" x="134" y="633" textLength="687" lengthAdjust="spacingAndGlyphs">WORK TOGETHER FOR GOOD</text>

  <text class="verse verse-tail" x="159" y="793" textLength="640" lengthAdjust="spacingAndGlyphs">TO THOSE WHO LOVE GOD, TO THOSE WHO ARE CALLED</text>
  <text class="verse verse-tail" x="311" y="851" textLength="343" lengthAdjust="spacingAndGlyphs">ACCORDING TO HIS PURPOSE</text>

  <line class="rule" x1="298" y1="1132" x2="350" y2="1132" stroke-width="2"/>
  <text class="verse verse-reference" x="370" y="1147" textLength="216" lengthAdjust="spacingAndGlyphs">ROMANS 8:28</text>
  <line class="rule" x1="601" y1="1132" x2="653" y2="1132" stroke-width="2"/>
</svg>
</body>
</html>
```